Introduction of new dentist and new treatments

We want inform our Patients of our new dentist and new treatment methods. It is dealing about biologic dentistry and holistic dentistry. we are in switzerland and speak german

Font styles to use
Sans Serif

Colors
00a990
33b8a4
9bcb3c
acd036
cadf82
0292cd
3176b5
e34297
e667a6

Requirements
Must have
• Text, which can be edited. It will be in german
• Name of the dental clinic is
• "Brivana - Ihr Zahnarzt in Zug"
Nice to have
• A4 Layout

```html
<!DOCTYPE html>
<html lang="de">
<head>
<meta charset="utf-8">
<title>Brivana – Interdisziplinäre Zahnmedizin</title>
<link href="https://fonts.googleapis.com/css2?family=Noto+Serif:wght@400;700&family=Open+Sans:wght@400;600&display=swap" rel="stylesheet">
<style>
  :root{
    --blue:#3176b5;
    --navy:#1f3566;
    --green:#9bcb3c;
    --pink:#e34297;
    --text:#2b2b2b;
    --bg:#e9e9e9;
    --white:#ffffff;
  }
  *{margin:0;padding:0;box-sizing:border-box}
  html,body{width:1200px;height:1200px;overflow:hidden;background:var(--bg)}
  .flyer{position:absolute;left:222px;top:66px;width:756px;height:1068px;background:var(--white);
    font-family:"Noto Serif",serif;color:var(--text);overflow:hidden}
  .hero{position:absolute;left:0;top:0}
  .brand{position:absolute;left:508px;top:482px;text-align:center;width:210px}
  .brand-name{font-family:"Noto Serif",serif;font-size:24px;letter-spacing:5px;color:var(--navy);font-weight:400;line-height:1.2}
  .brand-tag{font-family:"Open Sans",sans-serif;font-size:10.5px;color:var(--navy);margin-top:4px}
  .content{position:absolute;left:34px;top:552px;width:692px}
  .headline{font-size:22.5px;line-height:26px;color:var(--blue);
    font-weight:700;letter-spacing:1.3px;text-align:justify;text-align-last:left}
  .lead{margin-top:10px;font-size:13.4px;line-height:17.4px;color:var(--pink)}
  .columns{margin-top:12px;display:grid;grid-template-columns:332px 340px;column-gap:20px}
  .section h2{font-size:13px;line-height:15px;color:var(--blue);font-weight:700;padding-left:18px;position:relative;margin-bottom:5px}
  .section h2::before{content:"";position:absolute;left:2px;top:4px;width:7px;height:7px;border-radius:50%;
    background:var(--pink);box-shadow:0 0 0 1.5px #f4b6d7}
  .section p{font-size:9.8px;line-height:12.6px;text-align:justify}
  .section + .section{margin-top:8px}
  .mark{color:var(--pink);font-weight:700}
  .struck{text-decoration:line-through;color:#888}
  .contact-bar{position:absolute;left:0;top:984px;width:756px;height:84px;background:var(--blue);color:var(--white);display:flex;align-items:center}
  .contact{display:flex;align-items:center;height:64px}
  .contact-phone{padding-left:34px;width:322px;gap:12px;font-size:30px;font-weight:700}
  .contact-address{padding-left:20px;width:208px;gap:16px;font-size:16.5px;line-height:1.3;border-left:1.5px solid var(--white);height:66px}
  .contact-web{padding-left:20px;gap:11px;font-family:"Open Sans",sans-serif;font-size:13.5px;border-left:1.5px solid var(--white);height:66px}
</style>
</head>
<body>
<main class="flyer">
  <svg class="hero" width="756" height="548" viewBox="0 0 827 600">
    <defs>
      <linearGradient id="teamTone" x1="0" y1="0" x2="1" y2="1">
        <stop offset="0" stop-color="#f1e6e2"/>
        <stop offset="0.45" stop-color="#8fb0dc"/>
        <stop offset="1" stop-color="#6f95cf"/>
      </linearGradient>
      <linearGradient id="portraitTone" x1="0" y1="0" x2="0" y2="1">
        <stop offset="0" stop-color="#c9c9cb"/>
        <stop offset="0.7" stop-color="#b59a8a"/>
        <stop offset="1" stop-color="#2d6cc0"/>
      </linearGradient>
    </defs>
    <path role="img" aria-label="Teamfoto des Praxisteams in Berufskleidung" fill="url(#teamTone)"
      d="M10,220 C8,110 30,30 90,0 L640,0 C700,60 715,200 700,400 C640,500 520,535 420,530 C250,515 60,400 10,240 Z"/>
    <path class="swoosh-green" fill="#9bcb3c"
      d="M0,200 C40,440 250,605 440,598 C570,592 640,520 668,430 C600,505 520,540 420,532 C250,518 60,400 0,262 Z"/>
    <path class="swoosh-blue" fill="#3176b5"
      d="M510,0 L758,0 C778,120 762,260 700,400 C716,260 704,120 640,50 C600,20 560,8 510,0 Z"/>
    <circle role="img" aria-label="Porträtfoto des neuen Zahnarztes" cx="158" cy="463" r="123"
      fill="url(#portraitTone)" stroke="#3176b5" stroke-width="4"/>
  </svg>

  <div class="brand">
    <div class="brand-name">BRIVANA</div>
    <div class="brand-tag">Ihr Zahnarzt in Zug</div>
  </div>

  <div class="content">
    <h1 class="headline">Interdisziplinäre Zahnmedizin - Zusammenhang zwischen Zahnproblemen und der Gesundheit von Körper und Geist</h1>
    <p class="lead">Zahn und Gesundheit haben eins gemeinsam – Man vermisst sie, wenn sie fehlt. Zähne haben einen engen Zusammenhang zur Gesundheit und können diese beeinflussen. Sowohl negativ als auch positiv.</p>

    <div class="columns">
      <div class="col col-left">
        <section class="section">
          <h2>Funktion des Kauorgans und interdisziplinäre Zahnmedizin</h2>
          <p>„Funktion ist nicht alles. Aber ohne Funktion ist alles nichts!“ Sagte einst Prof.M.Keller (Zahnarzt, Gnathologie) und betonte die Bedeutung der Funktion des Kausystems. Sprechen, Kauen aber auch Körperhaltung und Stressmanagement gehören zu den Funktionen der Zähne. Ein gut funktionierendes Kauorgan (nach Prof.L. Brandt, interdisziplinäre Zahnmedizin) kann Stress bewältigen und mehr Leistung und Wohlbefinden bringen. Sehr oft erkennt man Funktionsstörungen daran, dass die Zähne nicht richtig zueinander passen oder Muskelverspannungen und Schmerzen im Kiefergelenk auftreten.</p>
        </section>
        <section class="section">
          <h2>Zahnverlust und neurologische Auswirkung</h2>
          <p>Ein physiologisches Kausystem hat sehr feine Steuerungs- und Wahrnehmungsmöglichkeiten. Bei Zahnverlust werden diese Fähigkeiten weniger benötigt. Weniger gebrauchte Ressourcen werden von der Natur dementsprechend abgebaut. Studien zeigen, dass Menschen mit weniger Zähnen mehr Risiko zur Bildung von Demenz bergen.</p>
        </section>
      </div>

      <div class="col col-right">
        <section class="section">
          <h2>Parodontitis und systemische Erkrankungen</h2>
          <p>Parodontitis (Entzündung des Zahnhalteapparats) ist eine der häufigsten chronischen Krankheiten weltweit und daher gut erforscht. Herzkrankheiten, Diabetes und Frühgeburtlichkeit sind einige der systemischen Krankheiten mit der Parodontitis in Zusammenhang steht. <span class="mark">Zahnfleischbluten, Zahnlockerung, Zahnfleischschwund und Zahnverlust sind typische Begleiterscheinungen von Parodontitis.</span> Eine systematische Parodontitis-Behandlung kann <span class="struck">auch</span> positive Auswirkungen auf die gesamte Gesundheit haben.</p>
        </section>
        <section class="section">
          <h2>Ganzheitliche Erklärungen</h2>
          <p>Die komplementäre Zahnheilkunde, sehr oft auch als ganzheitliche oder biologische Zahnheilkunde bezeichnet, versucht mit Hilfe von Meridianen (Traditionelle Chinesische Medizin), den Zusammenhang zwischen Zähnen und anderen Organen und Körperteilen zu erklären. Es gibt immer mehr Patienten und Zahnärzte die von dieser Theorie und deren Ergebnissen überzeugt sind. Aufgrund der wissenschaftlichen Lage ist eine ausführliche Aufklärung vor der Behandlung sehr ratsam.</p>
        </section>
      </div>
    </div>
  </div>

  <footer class="contact-bar">
    <div class="contact contact-phone">
      <svg width="32" height="32" viewBox="0 0 34 34" aria-hidden="true">
        <circle cx="17" cy="17" r="15" fill="none" stroke="#fff" stroke-width="2.5"/>
        <path d="M11,9 L14,9 L15.5,13 L13.5,14.5 C14.5,17 16.5,19 19,20 L20.5,18 L24.5,19.5 L24.5,22.5 C24.5,23.5 23.5,24.5 22.5,24.5 C15,24 10,19 9.5,11 C9.5,10 10,9 11,9 Z" fill="#fff"/>
      </svg>
      <span>+41415550219</span>
    </div>
    <div class="contact contact-address">
      <svg width="18" height="26" viewBox="0 0 20 28" aria-hidden="true">
        <path d="M10,0 C4.5,0 0,4.5 0,10 C0,17 10,28 10,28 C10,28 20,17 20,10 C20,4.5 15.5,0 10,0 Z M10,14 A4,4 0 1 1 10,6 A4,4 0 1 1 10,14 Z" fill="#fff"/>
      </svg>
      <span>Zahnarztpraxis<br>Seestrasse<br>14, 6300 Zug</span>
    </div>
    <div class="contact contact-web">
      <svg width="20" height="20" viewBox="0 0 22 22" aria-hidden="true" fill="none" stroke="#fff" stroke-width="1.6">
        <circle cx="11" cy="11" r="9.5"/>
        <ellipse cx="11" cy="11" rx="4.5" ry="9.5"/>
        <line x1="1.5" y1="11" x2="20.5" y2="11"/>
        <line x1="3" y1="6" x2="19" y2="6"/>
        <line x1="3" y1="16" x2="19" y2="16"/>
      </svg>
      <span>www.brivana-zug.ch</span>
    </div>
  </footer>
</main>
</body>
</html>
```